plumbing & gas fitting business card design

We need a business card design for a plumbing & gas fitting company. The company covers commercial, domestic and maintenance work. We would like a modern design communicating efficiency and sophistication. preferred colours would include (red grey & black) or (green grey & black). Please DO NOT include any water droplets.

Varcoe Plumbing & Gas, Commercial Domestic & Maintenance, licence no. 418736K, ABN 57204918362, Phone 0417382965, Email varcoeplumbingandgas@tidemail.com

```html
<!DOCTYPE html>
<html lang="en">
<head>
<meta charset="utf-8">
<title>Varcoe Plumbing &amp; Gas — Business Card</title>
<link rel="stylesheet" href="https://fonts.googleapis.com/css2?family=Questrial&display=swap">
<style>
  :root {
    --backdrop: #8e8f91;
    --card-grey: #a9aaac;
    --card-white: #f4f4f2;
    --brand-red: #c8141c;
    --ink: #1b1b1d;
    --rule-white: #f7f7f7;
    --shadow: rgba(0, 0, 0, 0.28);
  }
  * { box-sizing: border-box; margin: 0; padding: 0; }
  html, body {
    width: 1200px;
    height: 1000px;
    overflow: hidden;
    background: var(--backdrop);
    font-family: "Questrial", "Century Gothic", sans-serif;
  }
  .canvas { position: relative; width: 1200px; height: 1000px; }

  .card {
    position: absolute;
    width: 660px;
    height: 403px;
    box-shadow: 0 10px 28px var(--shadow);
  }

  /* Back of card: contact details */
  .card-back {
    left: 460px;
    top: 80px;
    background: var(--card-white);
    color: var(--ink);
  }
  .card-back .services {
    position: absolute;
    left: 56px;
    top: 58px;
    font-size: 23px;
    line-height: 1.18;
  }
  .card-back .accent-rule {
    position: absolute;
    left: 44px;
    right: 0;
    top: 156px;
    height: 6px;
    background: var(--brand-red);
  }
  .card-back .contact {
    position: absolute;
    left: 56px;
    top: 186px;
    font-size: 23px;
    line-height: 1.22;
  }
  .card-back .contact .email { color: var(--brand-red); }

  /* Front of card: brand */
  .card-front {
    left: 80px;
    top: 520px;
    background: var(--card-grey);
  }
  .brand-row {
    position: absolute;
    left: 0;
    right: 0;
    top: 50%;
    transform: translateY(-50%);
    display: flex;
    align-items: center;
  }
  .brand-row .rule {
    height: 6px;
    background: var(--rule-white);
  }
  .brand-row .rule-lead { width: 70px; }
  .brand-row .rule-tail { flex: 1; }
  .brand-mark {
    width: 58px;
    height: 58px;
    margin: 0 22px;
    background: var(--brand-red);
  }
  .brand-name {
    font-size: 40px;
    color: var(--ink);
    white-space: nowrap;
    margin-right: 22px;
    letter-spacing: 0.5px;
  }
</style>
</head>
<body>
<main class="canvas">
  <section class="card card-back" aria-label="Business card back">
    <p class="services">
      Commercial Domestic &amp; Maintenance<br>
      licence no. 418736K<br>
      ABN 57204918362
    </p>
    <div class="accent-rule"></div>
    <p class="contact">
      Phone 0417382965<br>
      <span class="email">Email varcoeplumbingandgas@tidemail.com</span>
    </p>
  </section>

  <section class="card card-front" aria-label="Business card front">
    <div class="brand-row">
      <span class="rule rule-lead"></span>
      <span class="brand-mark"></span>
      <h1 class="brand-name" style="font-weight:400">Varcoe Plumbing &amp; Gas</h1>
      <span class="rule rule-tail"></span>
    </div>
  </section>
</main>
</body>
</html>
```